Business Card Design

We need a business card for a well established Semi Trailer Hire company. I am looking for a new start as we are moving so would like to update our Business Cards and Letter heads.
We hire Semi Trailers to Transport companies.
The colour of our Trailers are Cherry Red so this must be the prominent colour.
I do not want any pictures of trailers on the design.
I do not want the design to be flowery in anyway as we are in the transport industry.
Simple yet effective

Trovan Hire Pty Ltd
Ros Dunmore
Director
Ph: 03 9412 5083
Mobile: 0421 736 209
ros.dunmore@trovanhire.com.au
www.trovanhire.com.au
214-220 Pellow Road, Yarraville

```html
<!DOCTYPE html>
<html lang="en">
<head>
<meta charset="utf-8">
<title>Trovan Hire Pty Ltd – Business Card</title>
<link rel="stylesheet" href="https://fonts.googleapis.com/css2?family=Lato:wght@400;700;900&family=Arimo:wght@400;700&display=swap">
<style>
  :root {
    --cherry: #c1272d;
    --cherry-deep: #a91f25;
    --charcoal: #231f20;
    --ink: #2b2b2b;
    --grey: #7a7a7a;
    --paper: #ffffff;
    --backdrop: #e9e9e9;
  }
  * { box-sizing: border-box; margin: 0; padding: 0; }
  html, body {
    width: 1200px; height: 800px; overflow: hidden;
    background: var(--backdrop);
  }
  .canvas {
    position: relative; width: 1200px; height: 800px;
  }
  .card {
    position: absolute; top: 250px;
    width: 520px; height: 300px;
    overflow: hidden;
    background: var(--paper);
    box-shadow: 0 6px 18px rgba(0,0,0,.18);
  }
  .card--front { left: 50px; }
  .card--back  { left: 630px; }

  .band { position: absolute; left: 0; width: 100%; }
  .band--red { background: var(--cherry); }
  .band--dark { background: var(--charcoal); }

  .pattern-field {
    position: absolute;
    background: radial-gradient(ellipse at center, rgba(255,255,255,.32), rgba(255,255,255,0) 70%);
  }

  .brand {
    position: absolute; display: flex; align-items: center; gap: 12px;
    font-family: "Lato", sans-serif; font-weight: 900;
    color: var(--cherry); white-space: nowrap; letter-spacing: -.3px;
  }
  .brand__mark { background: var(--cherry); flex: none; }

  /* front */
  .card--front .brand { left: 40px; top: 121px; font-size: 32px; }
  .card--front .brand__mark { width: 34px; height: 34px; }

  /* back */
  .card--back .brand { left: 24px; top: 58px; font-size: 26px; }
  .card--back .brand__mark { width: 26px; height: 26px; }

  .contact-direct {
    position: absolute; right: 22px; top: 58px; text-align: right;
    font-family: "Arimo", sans-serif; color: var(--ink);
  }
  .contact-direct__mobile { font-size: 20px; font-weight: 700; letter-spacing: .5px; }
  .contact-direct__email { font-size: 11px; font-weight: 700; margin-top: 3px; }

  .person {
    position: absolute; left: 26px; top: 112px;
    font-family: "Lato", sans-serif;
  }
  .person__name { font-size: 25px; font-weight: 700; color: var(--ink); line-height: 1.1; }
  .person__role { font-size: 15px; color: var(--grey); }

  .rule { position: absolute; left: 0; width: 100%; background: var(--charcoal); }

  .address {
    position: absolute; left: 26px; bottom: 18px;
    font-family: "Arimo", sans-serif; font-size: 14px; line-height: 17px;
    color: var(--paper); font-style: normal;
  }
</style>
</head>
<body>
<main class="canvas">

  <section class="card card--front" aria-label="Card front">
    <div class="band band--red" style="top:0;height:95px;"></div>
    <div class="band band--red" style="top:185px;height:115px;"></div>
    <div class="pattern-field" role="img" aria-label="Scattered translucent white squares pattern" style="left:20px;top:8px;width:340px;height:86px;"></div>
    <div class="pattern-field" role="img" aria-label="Scattered translucent white squares pattern" style="left:300px;top:190px;width:210px;height:90px;"></div>
    <div class="brand"><span class="brand__mark"></span>Trovan Hire Pty Ltd.</div>
  </section>

  <section class="card card--back" aria-label="Card back">
    <div class="band band--dark" style="top:0;height:44px;"></div>
    <div class="brand"><span class="brand__mark"></span>Trovan Hire Pty Ltd.</div>
    <div class="contact-direct">
      <div class="contact-direct__mobile">0421 736 209</div>
      <div class="contact-direct__email">ros.dunmore@trovanhire.com.au</div>
    </div>
    <div class="person">
      <div class="person__name">Ros Dunmore</div>
      <div class="person__role">Director</div>
    </div>
    <div class="rule" style="top:172px;height:6px;"></div>
    <div class="band band--red" style="top:184px;height:116px;"></div>
    <div class="pattern-field" role="img" aria-label="Scattered translucent white squares pattern" style="left:290px;top:188px;width:225px;height:80px;"></div>
    <address class="address">
      214-220 Pellow Road<br>
      Yarraville<br>
      tel: 03 9412 5083<br>
      www.trovanhire.com.au
    </address>
  </section>

</main>
</body>
</html>
```